West Australian based aspiring best selling novelist needs a book cover design

I have a completed manuscript for a fiction novel about 3 women whose partners work away in fly in fly out (FIFO) jobs. One woman has three young kids (boy, 8, boy 6 and girl 18months old), one woman is the first woman's sister and is young and beautiful but a bit troubled and one woman works on reception at a strip club. All three want to be independent but still miss their lovers. Location is the Midwest of Western Australia where there are beautiful beaches, blue skies and crayfish. The title is 'Seven Kites Over the Salt Flats.' Author's name is Ruth Dalby. I need a book cover design. I am unsure whether to try and capture the spirit of those women or the landscape or do a simple graphic design like crosses on a dateless calendar, counting down the days (Two weeks crossed off then one happy week when the lover is home and then another two sad weeks). The final design should lure people in to want to read the text. Thank you

Target Market(s)
Women, particularly those who are struggling with being a stay at home lover.

Must Have:
- Soul, an understanding of the complexity of loneliness. The women are strong and interesting- not flaky. This is NOT a romance novel. It is a quirky story with heart.

Nice to Have:
- A design that is striking but not too busy

Should Not Have:
- No trashy images of women. Should NOT look like a romance novel.

Target Market(s)

Women 18 upwards

Industry/Entity Type

Book Publisher

Font styles to use
Other font styles liked:
• unsure

Requirements
Must have
• A bit of quirkiness, soul, loneliness, independence
Nice to have
• Something striking but not too busy. I trust your skills!
Should not have
• Not look like a romance novel. The genre is more contemporary chick literature

```html
<!DOCTYPE html>
<html lang="en">
<head>
<meta charset="utf-8">
<title>Seven Kites Over the Salt Flats – Wraparound Cover</title>
<link rel="stylesheet" href="https://fonts.googleapis.com/css2?family=Kaushan+Script&family=Cinzel:wght@400&family=Rokkitt:wght@700&family=EB+Garamond:wght@400&display=swap">
<style>
  :root {
    --page-bg: #f4f3f0;
    --cover-dark: #262626;
    --cover-mid: #333230;
    --glow-warm: #8a7a5c;
    --glow-soft: #5a5244;
    --hill: #1c1c1c;
    --teal: #7fb3a6;
    --ink-light: #ecebe6;
    --placeholder: #cfcfcf;
    --blossom: #dfe9e4;
  }
  * { margin: 0; padding: 0; box-sizing: border-box; }
  html, body { width: 842px; height: 1200px; overflow: hidden; background: var(--page-bg); }

  .wraparound {
    position: absolute;
    left: 21px; top: 311px;
    width: 800px; height: 578px;
    background:
      radial-gradient(ellipse 70% 22% at 62% 86%, var(--glow-warm) 0%, var(--glow-soft) 35%, transparent 75%),
      linear-gradient(180deg, var(--cover-dark) 0%, var(--cover-mid) 70%, var(--cover-dark) 100%);
    overflow: hidden;
    color: var(--ink-light);
  }
  .hill-line { position: absolute; left: 0; top: 0; width: 800px; height: 578px; }

  /* Back cover */
  .back-cover { position: absolute; left: 0; top: 0; width: 386px; height: 578px; }
  .back-title {
    position: absolute; left: 70px; top: 32px; width: 250px;
    font-family: "Kaushan Script", cursive; font-size: 26px; line-height: 31px;
    color: var(--teal); text-align: center;
  }
  .story-outline {
    position: absolute; left: 67px; top: 170px; width: 260px;
    font-family: "Rokkitt", serif; font-weight: 700; font-size: 9.5px; line-height: 11.2px;
    color: var(--ink-light); list-style: none;
  }
  .story-outline .section { margin-bottom: 9px; }
  .story-outline .l2 { padding-left: 14px; }
  .story-outline .l3 { padding-left: 26px; }
  .author-photo {
    position: absolute; left: 31px; top: 408px; width: 54px; height: 66px;
    background: var(--placeholder);
  }
  .bio {
    position: absolute; left: 88px; top: 412px; width: 160px;
    font-family: "EB Garamond", serif; font-size: 9.5px; line-height: 12.4px; text-align: center;
  }
  .bio-name { font-family: "Cinzel", serif; font-size: 15px; line-height: 18px; color: var(--teal); }
  .bio-link {
    position: absolute; left: 30px; top: 484px; width: 220px;
    font-family: "EB Garamond", serif; font-size: 9.5px; line-height: 12px; text-align: center;
  }
  .copyright {
    position: absolute; left: 30px; top: 519px; width: 190px;
    font-family: "Cinzel", serif; font-size: 7px; line-height: 9.5px; text-align: center;
  }

  /* Spine */
  .spine { position: absolute; left: 386px; top: 0; width: 30px; height: 578px; }
  .spine-title {
    position: absolute; left: 3px; top: 45px; width: 24px; height: 270px;
    writing-mode: vertical-rl;
    font-family: "Kaushan Script", cursive; font-size: 13px; color: var(--teal);
    white-space: nowrap;
  }
  .spine-emblem {
    position: absolute; left: 5px; top: 336px; width: 20px; height: 62px;
    border: 1px solid #111; background: #3a3a3a;
  }
  .spine-author {
    position: absolute; left: 4px; top: 420px; width: 22px;
    writing-mode: vertical-rl;
    font-family: "Cinzel", serif; font-size: 16px; letter-spacing: 1px; white-space: nowrap;
  }

  /* Front cover */
  .front-cover { position: absolute; left: 416px; top: 0; width: 384px; height: 578px; }
  .front-author {
    position: absolute; left: 0; top: 32px; width: 384px; text-align: center;
    font-family: "Cinzel", serif; font-size: 29px; letter-spacing: 1px;
  }
  .plane-icon { position: absolute; left: 168px; top: 76px; width: 48px; height: 20px; }
  .front-title {
    position: absolute; left: 10px; top: 100px; width: 364px; text-align: center;
    font-family: "Kaushan Script", cursive; font-size: 44px; line-height: 52px; color: var(--teal);
  }
  .blossom-tree {
    position: absolute; left: 100px; top: 300px; width: 260px; height: 200px;
    background: radial-gradient(ellipse at 60% 45%, rgba(223,233,228,0.35) 0%, rgba(127,179,166,0.18) 40%, transparent 72%);
  }
  .tagline {
    position: absolute; left: 0; top: 526px; width: 384px; text-align: center;
    font-family: "Cinzel", serif; font-size: 11px; letter-spacing: 0.3px;
  }
</style>
</head>
<body>
  <main class="wraparound">
    <svg class="hill-line" viewBox="0 0 800 578" aria-hidden="true">
      <path d="M0 560 C 120 545, 230 505, 330 500 C 440 495, 520 470, 600 455 C 680 442, 760 470, 800 505 L 800 578 L 0 578 Z" fill="var(--hill)"/>
    </svg>

    <section class="back-cover">
      <h2 class="back-title">seven<br>kites over<br>the salt<br>flats</h2>
      <ol class="story-outline">
        <li class="section">I. Set the Stage
          <div class="l2">A. Introduce Your Hero</div>
          <div class="l3">1. What is his profession/role?</div>
          <div class="l3">2. What adjectives describe his character?</div>
          <div class="l3">3. What makes him interesting?</div>
          <div class="l2">B. Reveal the Setting</div>
          <div class="l3">1. If fantasy, what is this world like?</div>
          <div class="l3">2. If historical fiction, what is the time period &amp; location?</div>
          <div class="l2">C. Reveal the Current Situation</div>
          <div class="l3">1. What is the hero's life currently like?</div>
          <div class="l3">2. Does he have any dreams or desires that are about to be destroyed?</div>
        </li>
        <li class="section">II. Introduce the Problem
          <div class="l2">A. What issue turns the hero's life up-side down?</div>
          <div class="l2">B. What goal is the hero trying to achieve?</div>
          <div class="l2">C. What opposition stands in his way?</div>
          <div class="l2">D. What's at stake?</div>
        </li>
      </ol>
      <div class="author-photo" role="img" aria-label="Author portrait photograph"></div>
      <div class="bio">
        <div class="bio-name">RUTH DALBY</div>
        Is a novelist living in West Australia. She enjoys writing, reading and spending time with her family and friends at the beach.
      </div>
      <p class="bio-link">Please visit her author page for news<br>and more at www.ruthdalbywrites.com</p>
      <p class="copyright">SEVEN KITES OVER THE SALT FLATS<br>COPYRIGHT © 2016 BY RUTH DALBY<br>ALL RIGHTS RESERVED</p>
    </section>

    <section class="spine">
      <div class="spine-title">seven kites over the salt flats</div>
      <div class="spine-emblem" role="img" aria-label="Small blossom emblem"></div>
      <div class="spine-author">RUTH DALBY</div>
    </section>

    <section class="front-cover">
      <p class="front-author">RUTH DALBY</p>
      <svg class="plane-icon" viewBox="0 0 48 20" aria-hidden="true">
        <path d="M4 10 L40 9 Q47 10 40 11.5 L4 11 Z" fill="var(--ink-light)"/>
        <path d="M18 10 L28 2 L31 2 L25 10 Z M18 11 L28 18 L31 18 L25 11 Z M6 10 L3 5 L6 5 L10 10 Z" fill="var(--ink-light)"/>
      </svg>
      <h1 class="front-title">seven<br>kites over<br>the salt<br>flats</h1>
      <div class="blossom-tree" role="img" aria-label="Wind-bent tree with white blossoms blowing off a hilltop"></div>
      <p class="tagline">A NOVEL OF LOVE , INDEPENDENCE AND YEARNING.</p>
    </section>
  </main>
</body>
</html>
```